Poster & Flyer - Golf Tournament

Poster and Flyer (2 sperapate) is required for an upcoming Tervane Open Golf Tournament. Although this tournament is amongst friends only (normally 40 people) we want to announce this years (13th year) tournament a bit differently.

* Poster should grab the players (brief outline)
* Flyer should have more detail and graphics
* Design flows in each Poster/Flyer.

There are several components to the Tournament that include:

1. Tournament Logo
2. Prizes (Set of golf clubs and Hotel Accommodation)
3. FairwayLedger App (Live leaderboard)
4. Timetable of events and golf
5. Venue of Golf Tournament
6. Payment terms

All information relating to components are attached.

1. Tournament Logo - Some brief background, The "Tervane" was religious compass like symbol that basically pointed the people in the right direction when they were being faithful. We have incorporated the Logo with a golf tournament :-).

2. 1st Prize - full set of Fitted Brindle VEX Arc Pro Golf Clubs with VEX Golf Bag (Worth $2, 200 RRP)

2nd Prize - 2 nights 5 Star Accommodation at any Marrow Hotel in Australia includes Breakfast. (Worth $700 RRP).

Fairway Ledger is a free mobile Golf app that will take the Tervane Open to another level.

Easy mobile live scoring, leaderboards, chat, stats & social interactions - all real time with all popular game formats.

Bring it On!

More info go to http://www.fairwayledger-example.com/

* Can you incorporate some graphics from website in Poster and Flyer.

4. Timetable document attached. Make it presentable on the Flyer.

5. If we can incorporate aspects (graphics) of the golf course e.g. Golf Course Logo's, signature holes etc.

Go to:

a. Bramble Hollow Course - http://www.bramblehollow-example.com.au
b. Port Welden Golf Resort - https://www.mtlo-example.com.au/wps/wcm/connect/mtlo/Resorts/MTLO+Resorts/MTLO+Port+Welden+Resort/Port+Welden+Golf

If you go to google images I'm sure you can find further images relating to the golf course.

6. Payment terms: Can you please express the "early bird special"

Also I will need a extra poster without the "early bird special" once the time runs out.

If you have any further questions please do not hesitate to drop me an email.

* Please note - I will end Project early if I find a design I desire.
Updates

Please add "like us on facebook" logo (see attached)

facebook link is - http://www.socialpage-example.com/Tervaneopen

Industry/Entity Type

Golf Course

```html
<!DOCTYPE html>
<html lang="en">
<head>
<meta charset="utf-8">
<title>Tervane Open Golf Tournament Flyer</title>
<link rel="stylesheet" href="https://fonts.googleapis.com/css2?family=Raleway:wght@300;400;500;600;700;800&display=swap">
<style>
  :root {
    --green: #5b8f2c;
    --green-dark: #2f6b1c;
    --ink: #3d3d3d;
    --ink-soft: #5a5a5a;
    --paper: #ffffff;
    --ball-shade: #d9d9d9;
    --edge: #1b1b1b;
    --tag-bg: #3b3b3b;
    --gold: #b08d3c;
  }
  * { margin: 0; padding: 0; box-sizing: border-box; }
  html, body { width: 900px; height: 1200px; overflow: hidden; background: #f2f2f2; }
  body { font-family: "Raleway", Arial, sans-serif; color: var(--ink); }
  .flyer { position: relative; width: 900px; height: 1200px; overflow: hidden; background: var(--paper); }
  .flyer-art { position: absolute; inset: 0; }
  .block { position: absolute; }

  .ball-label { position: absolute; text-align: center; line-height: 1; }
  .ball-label .light { display: block; font-weight: 400; color: var(--green); font-size: 34px; }
  .ball-label .bold { display: block; font-weight: 700; color: var(--ink-soft); font-size: 38px; }
  .label-year { left: 20px; top: 80px; width: 140px; }
  .label-year .light { font-size: 30px; color: var(--ink-soft); }
  .label-year .bold { font-weight: 400; color: var(--green); font-size: 34px; }
  .label-price { left: 14px; top: 310px; width: 160px; }
  .label-app { left: 14px; top: 572px; width: 150px; }
  .label-app .light { font-size: 36px; }

  .event-title { left: 200px; top: 92px; text-align: center; width: 170px; line-height: 1; white-space: nowrap; }
  .event-title .top { display: block; font-weight: 700; color: var(--green); font-size: 22px; }
  .event-title .bottom { display: block; font-weight: 400; color: var(--ink); font-size: 22px; letter-spacing: 0.3px; }

  .early-tag { left: 204px; top: 280px; width: 180px; height: 28px; background: var(--tag-bg); color: #fff;
    font-size: 14px; font-weight: 700; text-align: center; line-height: 28px; letter-spacing: 0.3px;
    box-shadow: 0 2px 3px rgba(0,0,0,.35); }
  .early-tag span { font-weight: 400; }
  .payment-terms { left: 204px; top: 320px; width: 275px; font-size: 12.5px; line-height: 24px; color: var(--ink); white-space: nowrap; }
  .payment-terms strong { color: var(--green); }
  .payment-terms .note { color: var(--green-dark); font-weight: 500; }

  .app-name { left: 200px; top: 592px; width: 240px; text-align: center; line-height: 1; }
  .app-name .top { display: block; font-weight: 700; color: var(--ink-soft); font-size: 36px; }
  .app-name .bottom { display: block; font-weight: 400; color: var(--green); font-size: 36px; letter-spacing: 0.5px; }
  .app-name .url { display: block; font-weight: 600; color: var(--ink); font-size: 14px; margin-top: 2px; }

  .prize { position: absolute; line-height: 1; }
  .prize .rank { display: block; font-weight: 400; color: var(--green); font-size: 24px; }
  .prize .what { display: block; font-weight: 800; color: var(--ink); font-size: 30px; }
  .prize .detail { display: block; font-weight: 500; color: var(--ink-soft); font-size: 7.5px; margin-top: 2px; }
  .prize-first { left: 22px; top: 790px; text-align: center; width: 175px; }
  .prize-second { left: 188px; top: 978px; width: 180px; }

  .hotel-name { left: 28px; top: 1010px; width: 120px; text-align: center; font-size: 26px; font-weight: 700; color: #2b3a8c; }

  .timetable { left: 520px; top: 22px; width: 290px; text-align: center; color: #2f2f2f; }
  .timetable h3 { font-size: 17px; font-weight: 700; color: var(--green-dark); margin: 10px 0 6px; }
  .timetable ul { list-style: none; font-size: 11.5px; line-height: 16px; font-weight: 500; }
  .timetable li::before { content: "▪ "; color: #555; }

  .brand-mark { left: 520px; top: 1070px; width: 260px; text-align: center; color: var(--gold);
    font-size: 26px; font-weight: 600; letter-spacing: 3px; white-space: nowrap; }
</style>
</head>
<body>
<main class="flyer">
  <svg class="flyer-art" width="900" height="1200" viewBox="0 0 900 1200" xmlns="http://www.w3.org/2000/svg">
    <defs>
      <linearGradient id="course" x1="0" y1="0" x2="0" y2="1">
        <stop offset="0" stop-color="#dfe6ea"/>
        <stop offset="0.22" stop-color="#c9d5cf"/>
        <stop offset="0.32" stop-color="#7f9a5c"/>
        <stop offset="0.4" stop-color="#4c8a1f"/>
        <stop offset="0.5" stop-color="#c9b08a"/>
        <stop offset="0.58" stop-color="#6aa92a"/>
        <stop offset="0.75" stop-color="#3f8a1a"/>
        <stop offset="1" stop-color="#2f6e14"/>
      </linearGradient>
      <radialGradient id="ball-face" cx="0.15" cy="0.5" r="0.9">
        <stop offset="0.55" stop-color="#ffffff"/>
        <stop offset="0.85" stop-color="#f1f1f1"/>
        <stop offset="1" stop-color="#d9d9d9"/>
      </radialGradient>
      <radialGradient id="small-ball" cx="0.4" cy="0.4" r="0.7">
        <stop offset="0.5" stop-color="#ffffff"/>
        <stop offset="1" stop-color="#d6d6d6"/>
      </radialGradient>
      <linearGradient id="bag" x1="0" y1="0" x2="1" y2="1">
        <stop offset="0" stop-color="#1d2330"/>
        <stop offset="0.45" stop-color="#2b4fb0"/>
        <stop offset="0.7" stop-color="#e6e6e6"/>
        <stop offset="1" stop-color="#d5692a"/>
      </linearGradient>
    </defs>

    <rect class="course-photo" x="0" y="0" width="900" height="1200" fill="url(#course)" role="img" aria-label="Photo of a golf course: a player in a red shirt playing out of a sand bunker towards the flag, trees and sky behind"/>

    <path class="ball-panel" d="M0,0 L300,0 C560,230 610,720 440,1200 L0,1200 Z" fill="url(#ball-face)"/>
    <path class="ball-edge" d="M300,0 C560,230 610,720 440,1200" fill="none" stroke="#1b1b1b" stroke-width="9"/>
    <path class="ball-rim" d="M322,0 C582,230 632,720 462,1200" fill="none" stroke="#ffffff" stroke-width="3" opacity=".8"/>

    <g class="connectors" fill="none" stroke="#9a9a9a" stroke-width="1.6" stroke-dasharray="8 6">
      <path d="M92,180 C130,220 130,250 92,272"/>
      <path d="M92,415 C130,460 130,500 92,528"/>
      <path d="M150,660 C210,680 240,700 260,712"/>
      <path d="M230,860 C215,900 200,930 190,960"/>
    </g>

    <g class="ball-badges" stroke="#9e9e9e" stroke-width="3" fill="url(#small-ball)">
      <circle cx="82" cy="108" r="74"/>
      <circle cx="82" cy="343" r="74"/>
      <circle cx="82" cy="605" r="74"/>
    </g>

    <circle class="prize-photo" cx="290" cy="785" r="92" fill="url(#bag)" stroke="#8f8f8f" stroke-width="5" role="img" aria-label="Photo of golf bags in black, blue, white and orange"/>
    <circle class="hotel-badge" cx="88" cy="1026" r="66" fill="#ffffff" stroke="#a6a6a6" stroke-width="5"/>
  </svg>

  <div class="block ball-label label-year"><span class="light">13th</span><span class="bold">YEAR</span></div>
  <div class="block ball-label label-price"><span class="light">ONLY</span><span class="bold">595 $</span></div>
  <div class="block ball-label label-app"><span class="light">MOB</span><span class="bold">APP</span></div>

  <h1 class="block event-title"><span class="top">GOLF</span><span class="bottom">TOURNAMENT</span></h1>

  <div class="block early-tag">EARLY <span>BIRD</span> PRICE</div>
  <div class="block payment-terms">
    <p>a)Get a <strong>$65</strong> savings when you pay the total of<br><strong>$530</strong> upfront before 15th July 2013 .</p>
    <p>b)or Pay <strong>$300</strong> before the 30th June to<br>secure your place. The remaining <strong>$295</strong> to be<br>paid before the 30th Sept.</p>
    <p class="note">• &nbsp;Due to individual cancellations we can only<br>refund money if someone replaces your spot.</p>
  </div>

  <div class="block app-name"><span class="top">FAIRWAY</span><span class="bottom">LEDGER</span><span class="url">www.fairwayledger-example.com</span></div>

  <div class="prize prize-first"><span class="rank">1ST PLACE</span><span class="what">FULL SET</span><span class="detail">Fitted Brindle VEX Arc Pro Golf Clubs</span></div>
  <div class="block hotel-name">Marrow</div>
  <div class="prize prize-second"><span class="rank">2ND PLACE</span><span class="what">5* HOTEL</span><span class="detail">INCLUDING BREAKFAST</span></div>

  <section class="block timetable">
    <h3>Tuesday</h3>
    <ul>
      <li>Check in MTLO Port Welden Resort,<br>Harlow Reach Drive, Port Welden VIC 3990</li>
    </ul>
    <h3>Thursday</h3>
    <ul>
      <li>Buffet Breakfast – Port Welden</li>
      <li>am - Stroke - Port Welden</li>
      <li>pm - 4 man Ambrose</li>
      <li>Dinner &amp; Presentations</li>
    </ul>
    <h3>Wednesday</h3>
    <ul>
      <li>Buffet Breakfast – Port Welden</li>
      <li>am - Stableford - Bramble Hollow Golf Course</li>
      <li>pm - 4 man Ambrose</li>
      <li>Dinner – Port Welden</li>
      <li>Saltmere Hot Springs</li>
    </ul>
  </section>

  <div class="block brand-mark">TERVANE OPEN</div>
</main>
</body>
</html>
```